Tall Heron Vodka

We are launching a new mainstream Vodka brand "Tall Heron" to take on big brands. China will be first market. The category norms seems to be Red and Black on a clear bottle and we would expect some red but does not need to be entirely red. The design would need to work on both clear (Valdorin) and frosted (Pale Finch) style bottles. In the future we will have gold heron, silver heron, platinum heron and diamond heron for more premium variants.

Target Market(s)

China

Industry/Entity Type

Alcohol

Colors
EB3D1F
EC4F4E
F09395
F8D3D4
FCEDEE

Requirements
Must have
• Space for Chinese language as well ad English
Nice to have
• Energetic, Engaging
Should not have
• Not stereotypes of photo of bad looking bear. Good looking bear, light not heavy.

```html
<!DOCTYPE html>
<html lang="en">
<head>
<meta charset="utf-8">
<title>Tall Heron Label</title>
<link rel="stylesheet" href="https://fonts.googleapis.com/css2?family=Cinzel+Decorative:wght@700&family=Oswald:wght@400&family=Noto+Serif+SC:wght@600&display=swap">
<style>
  :root {
    --ink-red: #E2484B;
    --blush: #FCEDEE;
    --blush-deep: #F8D3D4;
    --rose: #F09395;
    --paper: #FFFFFF;
    --backdrop: #FFFFFF;
  }
  html, body {
    margin: 0;
    padding: 0;
    width: 1200px;
    height: 799px;
    overflow: hidden;
    background: var(--backdrop);
  }
  .canvas { display: block; width: 1200px; height: 799px; }
  .label-edge { fill: var(--paper); stroke: var(--blush-deep); stroke-width: 2; }
  .frame-line { fill: none; stroke: var(--ink-red); }
  .ornament-band { fill: url(#bandTone); }
  .emblem-area { fill: var(--rose); }
  .title-panel, .year-panel { fill: var(--paper); stroke: var(--ink-red); stroke-width: 3; }
  .brand-word {
    font-family: "Cinzel Decorative", serif;
    font-weight: 700;
    fill: var(--ink-red);
  }
  .brand-word-cn {
    font-family: "Noto Serif SC", serif;
    font-weight: 600;
    fill: var(--ink-red);
  }
  .year-text {
    font-family: "Oswald", sans-serif;
    fill: var(--ink-red);
  }
</style>
</head>
<body>
<svg class="canvas" viewBox="0 0 1200 799" xmlns="http://www.w3.org/2000/svg">
  <defs>
    <radialGradient id="bandTone" cx="50%" cy="50%" r="55%">
      <stop offset="0.6" stop-color="#FCEDEE"/>
      <stop offset="1" stop-color="#F8D3D4"/>
    </radialGradient>
  </defs>
  <g class="label">
    <ellipse class="label-edge" cx="600" cy="400" rx="262" ry="388"/>
    <ellipse class="frame-line" cx="600" cy="400" rx="246" ry="372" stroke-width="4"/>
    <ellipse class="frame-line" cx="600" cy="400" rx="236" ry="362" stroke-width="1.5"/>

    <ellipse class="ornament-band" cx="600" cy="400" rx="226" ry="350"
             role="img" aria-label="Engraved scrollwork border with fine hatched lines"/>
    <ellipse class="frame-line" cx="600" cy="400" rx="226" ry="350" stroke-width="2"/>

    <circle class="emblem-area" cx="600" cy="150" r="60"
            role="img" aria-label="Engraved heron emblem in a round medallion"/>
    <circle class="frame-line" cx="600" cy="150" r="66" stroke-width="2"/>

    <rect class="title-panel" x="396" y="238" width="408" height="322" rx="14"/>
    <text class="brand-word" x="600" y="338" font-size="84" text-anchor="middle"
          textLength="230" lengthAdjust="spacingAndGlyphs">TALL</text>
    <text class="brand-word" x="600" y="458" font-size="112" text-anchor="middle"
          textLength="360" lengthAdjust="spacingAndGlyphs">HERON</text>
    <text class="brand-word-cn" x="600" y="530" font-size="40" text-anchor="middle"
          letter-spacing="10" lang="zh-Hans">高鹭伏特加</text>

    <rect class="year-panel" x="468" y="574" width="264" height="70" rx="6"/>
    <text class="year-text" x="600" y="625" font-size="40" text-anchor="middle" letter-spacing="3">ESTD 2024</text>
  </g>
</svg>
</body>
</html>
```